Postcard design to acquire new clients for my Property Management Company

I'm looking for a postcard design that I can send to prospective clients detailing information about my company and services.
Postcard should be eye catching and contain information from www.brightkeyrentals-example.com. I've provided a few screen shots for the most important information and my logo.
Target Market(s)
Real Estate
Industry/Entity Type
Real Estate
Font styles to use
Sans Serif
Requirements
Must have
- Must be eye catching!! this will be a direct mail piece - I'd like for the card to be read and not tossed in the trash immediately.
Design que from the logo.
A place to write / print the receipts name and address.
our physical address - 2287 Marble Lane, Lubbock, TX 79555.
Should not have
- the contact information on the business card is not accurate - please use info from website.

```html
<!DOCTYPE html>
<html lang="en">
<head>
<meta charset="utf-8">
<title>BrightKey Rentals – Postcard</title>
<link rel="stylesheet" href="https://fonts.googleapis.com/css2?family=Playfair+Display:wght@400&family=Mulish:wght@300;400&family=Source+Sans+3:wght@400;600&display=swap">
<style>
  :root{
    --navy:#003350;
    --band:#094b8a;
    --ring-fill:#0b4a8c;
    --accent:#0a6ab4;
    --dot:#3fb6e8;
    --brand:#0d4f92;
    --white:#ffffff;
    --ink:#111111;
  }
  *{margin:0;padding:0;box-sizing:border-box}
  html,body{width:1200px;height:850px;overflow:hidden;background:var(--white)}
  .postcard{position:relative;width:1200px;height:850px;overflow:hidden;background:var(--white);font-family:"Source Sans 3",sans-serif}

  .offer-panel{position:absolute;left:0;top:0;width:757px;height:850px;background:var(--navy);color:var(--white)}
  .headline{position:absolute;left:88px;top:92px;font-family:"Playfair Display",serif;font-weight:400;font-size:46px;line-height:38px;letter-spacing:-0.2px}
  .plan-list{position:absolute;left:90px;top:196px;font-family:"Source Sans 3",sans-serif;font-size:21px;letter-spacing:0.1px}
  .plan-list b{font-weight:600;margin:0 3px}
  .accent-bar{position:absolute;left:90px;top:243px;width:44px;height:6px;background:var(--accent)}

  .rate-badge{position:absolute;left:88px;width:100px;height:100px}
  .rate-badge.lease{top:311px}
  .rate-badge.full{top:470px}
  .rate-badge.premium{top:628px}

  .tier-title{position:absolute;left:225px;font-family:"Playfair Display",serif;font-size:44px;line-height:1}
  .tier-tagline{position:absolute;left:226px;font-family:"Mulish",sans-serif;font-weight:300;font-size:23.5px;line-height:1}
  .tier-features{position:absolute;left:228px;list-style:none;font-family:"Mulish",sans-serif;font-weight:300;font-size:12.6px;line-height:15px}
  .tier-features li{position:relative;padding-left:11px;margin-bottom:13px}
  .tier-features li::before{content:"";position:absolute;left:0;top:50%;width:5px;height:5px;margin-top:-2px;border-radius:50%;background:var(--dot)}
  .tier-features b{font-weight:400;margin:0 1px}

  .mail-side .brand-name{position:absolute;left:823px;top:73px;font-family:"Source Sans 3",sans-serif;font-weight:600;font-size:21px;letter-spacing:3.2px;color:var(--brand)}
  .stamp-box{position:absolute;left:1067px;top:51px;width:77px;height:77px;border:1px solid var(--ink);display:flex;align-items:center;justify-content:center;text-align:center;font-size:15px;line-height:15px;color:var(--ink)}
  .greeting{position:absolute;left:825px;top:313px;font-size:24px;color:var(--brand);letter-spacing:0.2px}
  .address-line{position:absolute;height:1px;background:var(--ink)}
  .address-line.one{left:827px;top:421px;width:247px}
  .address-line.two{left:825px;top:470px;width:255px}
  .address-line.three{left:825px;top:517px;width:255px}

  .contact-band{position:absolute;left:0;top:790px;width:1200px;height:60px;background:var(--band);clip-path:polygon(356px 0,1200px 0,1200px 60px,297px 60px)}
  .contact-list{position:absolute;left:352px;top:808px;display:flex;align-items:center;gap:15px;color:var(--white);font-size:12.4px;white-space:nowrap}
  .contact-item{display:flex;align-items:center;gap:5px}
  .contact-item svg{flex:none}
</style>
</head>
<body>
<div class="postcard">

  <section class="offer-panel">
    <h1 class="headline">Choose the right property<br>management system.</h1>
    <p class="plan-list">LEASE ONLY<b>|</b>FULL SERVICE<b>|</b>PREMIUM</p>
    <div class="accent-bar"></div>

    <svg class="rate-badge lease" viewBox="0 0 100 100" aria-hidden="true">
      <circle cx="50" cy="50" r="44.5" fill="none" stroke="#fff" stroke-width="2.6" stroke-dasharray="116.4 23.3 124.2 15.5" transform="rotate(-30 50 50)"/>
      <circle cx="50" cy="50" r="37" fill="var(--ring-fill)"/>
      <text x="50" y="57" text-anchor="middle" font-family="Playfair Display, serif" font-size="31" fill="#fff">9%</text>
      <text x="50" y="68" text-anchor="middle" font-family="Mulish, sans-serif" font-size="6" fill="#fff">of annual lease</text>
    </svg>
    <h2 class="tier-title" style="top:301px">Lease.</h2>
    <p class="tier-tagline" style="top:343px">You Just Need Tenants.</p>
    <ul class="tier-features" style="top:389px">
      <li>Professional Photography<b>|</b>Marketing + Advertising<b>|</b>Property Showings</li>
      <li>Tenant Screening + Qualifications<b>|</b>Lease Execution<b>|</b>Move In Coordination</li>
    </ul>

    <svg class="rate-badge full" viewBox="0 0 100 100" aria-hidden="true">
      <circle cx="50" cy="50" r="44.5" fill="none" stroke="#fff" stroke-width="2.6" stroke-dasharray="116.4 23.3 124.2 15.5" transform="rotate(-30 50 50)"/>
      <circle cx="50" cy="50" r="37" fill="var(--ring-fill)"/>
      <text x="50" y="56" text-anchor="middle" font-family="Playfair Display, serif" font-size="27" fill="#fff">10%</text>
      <text x="50" y="67" text-anchor="middle" font-family="Mulish, sans-serif" font-size="6" fill="#fff">of monthly rent</text>
    </svg>
    <h2 class="tier-title" style="top:462px">Full Service</h2>
    <p class="tier-tagline" style="top:504px">Most Popular.</p>
    <ul class="tier-features" style="top:549px">
      <li>Leasing Service<b>|</b>24/7 Emergency Response<b>|</b>Move In &amp; Out Inspections<br>Pay All Invoices<b>|</b>Professional Lease Enforcement<b>|</b>Schedule + Oversee All Repairs</li>
      <li>Monthly + Year End Statements<b>|</b>Annual Market Rent Analysis</li>
    </ul>

    <svg class="rate-badge premium" viewBox="0 0 100 100" aria-hidden="true">
      <circle cx="50" cy="50" r="44.5" fill="none" stroke="#fff" stroke-width="2.6" stroke-dasharray="116.4 23.3 124.2 15.5" transform="rotate(-30 50 50)"/>
      <circle cx="50" cy="50" r="37" fill="var(--ring-fill)"/>
      <text x="50" y="56" text-anchor="middle" font-family="Playfair Display, serif" font-size="27" fill="#fff">12%</text>
      <text x="50" y="67" text-anchor="middle" font-family="Mulish, sans-serif" font-size="6" fill="#fff">of monthly rent</text>
    </svg>
    <h2 class="tier-title" style="top:632px">Premium</h2>
    <p class="tier-tagline" style="top:673px">Our Premier Service.</p>
    <ul class="tier-features" style="top:718px">
      <li>Includes Full Service Features<b>|</b>Professional Video Marketing<b>|</b><br>Home Warranty Coordination<b>|</b>Tenant Retention Program</li>
    </ul>
  </section>

  <section class="mail-side">
    <p class="brand-name">BRIGHTKEY RENTALS</p>
    <div class="stamp-box">STAMP<br>GOES<br>HERE</div>
    <p class="greeting">LET’S WORK</p>
    <div class="address-line one"></div>
    <div class="address-line two"></div>
    <div class="address-line three"></div>
  </section>

  <div class="contact-band"></div>
  <ul class="contact-list">
    <li class="contact-item">
      <svg width="12" height="20" viewBox="0 0 12 20" aria-hidden="true"><rect x="1" y="1" width="10" height="18" rx="2" fill="none" stroke="#fff" stroke-width="1.2"/><line x1="1" y1="4" x2="11" y2="4" stroke="#fff"/><line x1="1" y1="15" x2="11" y2="15" stroke="#fff"/><circle cx="6" cy="17" r="0.9" fill="#fff"/></svg>
      <span>(806) 555-0142</span>
    </li>
    <li class="contact-item">
      <svg width="20" height="20" viewBox="0 0 20 20" aria-hidden="true"><circle cx="10" cy="10" r="3.6" fill="none" stroke="#fff" stroke-width="1.6"/><path d="M13.6 7v4.2c0 2 2.8 2 3.2 0A7.6 7.6 0 1 0 13 16.8" fill="none" stroke="#fff" stroke-width="1.6"/></svg>
      <span>info@brightkeyrentals-example.com</span>
    </li>
    <li class="contact-item">
      <svg width="20" height="20" viewBox="0 0 20 20" aria-hidden="true"><circle cx="10" cy="10" r="8.5" fill="none" stroke="#fff" stroke-width="1.3"/><ellipse cx="10" cy="10" rx="3.8" ry="8.5" fill="none" stroke="#fff" stroke-width="1"/><line x1="1.5" y1="10" x2="18.5" y2="10" stroke="#fff" stroke-width="1"/></svg>
      <span>www.brightkeyrentals-example.com</span>
    </li>
    <li class="contact-item">
      <svg width="14" height="20" viewBox="0 0 14 20" aria-hidden="true"><path d="M7 19S1.5 11.5 1.5 7a5.5 5.5 0 0 1 11 0C12.5 11.5 7 19 7 19z" fill="none" stroke="var(--dot)" stroke-width="1.2"/><circle cx="7" cy="7" r="1.6" fill="none" stroke="var(--dot)"/></svg>
      <span>2287 Marble Lane, Lubbock, TX 79555</span>
    </li>
  </ul>

</div>
</body>
</html>
```